Update Business Card Design

I'm looking to update my business cards. Attached is a photo of the current design. I like the black side so that does not have to be update. The white side needs to be updated. I want the design to be modern and minimalistic.
I am a lawyer and my firm's website is www.brennoxlegalco.com (for reference).
My firm's logo has a horizontal version (which is on the black side of the card) and a vertical version (on the white side). I would prefer to keep the vertical version on the white side and horizontal version on the black side (the logo files are attached).

I am open to redesigning the black side also. I would like one side to have the horizontal logo and the other to have the vertical logo.

```html
<!DOCTYPE html>
<html lang="en">
<head>
<meta charset="utf-8">
<title>Brennox Legal Co. – Business Card</title>
<link rel="stylesheet" href="https://fonts.googleapis.com/css2?family=Montserrat:wght@400;500;700&display=swap">
<style>
  :root {
    --backdrop: #6e5c49;
    --card-white: #ffffff;
    --brand-cyan: #1ab8e2;
    --ink-dark: #464a4f;
    --ink-body: #222426;
    --card-black-start: #3a3a3a;
    --card-black-end: #000000;
    --rule-grey: #7a7a7a;
  }
  html, body {
    margin: 0;
    padding: 0;
    width: 916px;
    height: 1200px;
    overflow: hidden;
    background: var(--backdrop);
    font-family: "Montserrat", Arial, sans-serif;
  }
  .sheet { position: relative; width: 916px; height: 1200px; }

  .card {
    position: absolute;
    border-radius: 26px;
    overflow: hidden;
    box-shadow: 0 4px 14px rgba(0,0,0,.45);
  }
  .card--front { left: 73px; top: 108px; width: 770px; height: 460px; background: var(--card-white); }
  .card--back  { left: 71px; top: 640px; width: 775px; height: 464px;
    background: linear-gradient(90deg, var(--card-black-start) 0%, #1c1c1c 50%, var(--card-black-end) 60%, var(--card-black-end) 100%); }

  .front-accent { position: absolute; left: 0; top: 0; }

  .brand {
    position: absolute;
    display: flex;
    align-items: center;
    gap: 14px;
    white-space: nowrap;
  }
  .brand__dot { border-radius: 50%; background: var(--brand-cyan); flex: none; }
  .brand__rule { background: var(--rule-grey); flex: none; }
  .brand__name { font-weight: 500; letter-spacing: .04em; line-height: 1.05; }

  .brand--front { left: 407px; top: 62px; }
  .brand--front .brand__dot { width: 40px; height: 40px; }
  .brand--front .brand__rule { width: 2px; height: 70px; }
  .brand--front .brand__name { font-size: 27px; color: var(--ink-dark); }

  .brand--back { left: 138px; top: 155px; gap: 22px; }
  .brand--back .brand__dot { width: 100px; height: 100px; }
  .brand--back .brand__rule { width: 2px; height: 140px; background: #555; }
  .brand--back .brand__name { font-size: 46px; color: var(--brand-cyan); }

  .person { position: absolute; left: 418px; top: 218px; }
  .person__name { margin: 0; font-size: 26px; font-weight: 700; color: var(--ink-dark); letter-spacing: .01em; }
  .person__name .surname { color: var(--brand-cyan); }
  .person__title { margin: 4px 0 0; font-size: 16px; color: var(--ink-body); }

  .address { position: absolute; left: 422px; top: 294px; margin: 0; font-style: normal; font-size: 16px; line-height: 22px; color: var(--ink-body); }

  .contacts { position: absolute; left: 420px; top: 350px; margin: 0; padding: 0; list-style: none; font-size: 16px; color: var(--ink-body); }
  .contacts li { display: flex; align-items: center; gap: 9px; height: 24px; }
  .contacts svg { width: 17px; height: 17px; fill: var(--brand-cyan); flex: none; }
</style>
</head>
<body>
<main class="sheet">
  <section class="card card--front" aria-label="Card front">
    <svg class="front-accent" width="380" height="460" viewBox="0 0 380 460" aria-hidden="true">
      <circle cx="90" cy="230" r="230" fill="var(--brand-cyan)"/>
    </svg>

    <div class="brand brand--front">
      <span class="brand__dot"></span>
      <span class="brand__rule"></span>
      <span class="brand__name">BRENNOX<br>LEGAL CO.</span>
    </div>

    <div class="person">
      <h1 class="person__name">Darian <span class="surname">Kessler</span></h1>
      <p class="person__title">Attorney at Law</p>
    </div>

    <address class="address">318 N. Alder Drive, Suite 410<br>Westbrook, CA 90417</address>

    <ul class="contacts">
      <li><svg viewBox="0 0 24 24"><path d="M6.6 10.8a15.1 15.1 0 0 0 6.6 6.6l2.2-2.2c.3-.3.7-.4 1-.2 1.1.4 2.3.6 3.6.6.6 0 1 .4 1 1V20c0 .6-.4 1-1 1A17 17 0 0 1 3 4c0-.6.4-1 1-1h3.5c.6 0 1 .4 1 1 0 1.3.2 2.5.6 3.6.1.3 0 .7-.2 1z"/></svg>555.214.3068</li>
      <li><svg viewBox="0 0 24 24"><path d="M3 9c0-3 4-5 9-5s9 2 9 5v1h-5V8H8v2H3zM6 11h12l2 8v2H4v-2zm3 3v2h2v-2zm4 0v2h2v-2z"/></svg>555.386.1047</li>
      <li><svg viewBox="0 0 24 24"><path d="M7 3h10v5H7zM4 9h16v8h-3v4H7v-4H4zm5 6v4h6v-4z"/></svg>555.386.1052</li>
      <li><svg viewBox="0 0 24 24"><path d="M2 5h20v14H2zm2 2v1l8 5 8-5V7l-8 5z"/></svg>darian@BrennoxLegalCo.com</li>
    </ul>
  </section>

  <section class="card card--back" aria-label="Card back">
    <div class="brand brand--back">
      <span class="brand__dot"></span>
      <span class="brand__rule"></span>
      <span class="brand__name">BRENNOX<br>LEGAL CO.</span>
    </div>
  </section>
</main>
</body>
</html>
```